Basic images needed for business powerpoint slides

We need basic images for a powerpoint design. The designs should be clean, modern, simple and easy to read on a screen and if they were printed on paper. The images should not be overly designed (no fancy graphics or ornate fonts), but should still look professional.

Please pay attention to the attachments that have sketches of the images that are needed. In the notes section of the powerpoint slides specifies additional details for each image.

Also, please adhere to the design guidelines that are also uploaded. Only use colors and fonts that are specified. The final images should be similar to the look and feel of the images in the design guidelines.
Updates

Designers -
Thanks for all your submissions! I am reviewing all the designs with my team and will have a decision ready by Sunday evening. If you are submitting any new designs, please submit by Sunday morning EST so my team can review them.

Thanks!

Target Market(s)

business executives

Industry/Entity Type

Business

Requirements
Must have
• Must Have:
- 1. Please see the attached powerpoint for the sketches we would like to have recreated. There are specific notes in each slide with additional details.

2. Please refer to the following pages in the uploaded design guideline document:
Colors - p. 14
- Use either the bright or muted color options as specified in the color scheme on this page

Typography - p. 16-17
- Use either helvetica or arial options

Powerpoint guidelines - p.42
- see for example of the general look and feel of the company

```html
<!DOCTYPE html>
<html lang="en">
<head>
<meta charset="utf-8">
<title>Stakeholder Ring Slides</title>
<link href="https://fonts.googleapis.com/css2?family=Arimo:wght@400;700&display=swap" rel="stylesheet">
<style>
  :root {
    --page: #ffffff;
    --slide: #e7e7e8;
    --orange: #f0902a;
    --teal: #4fc2c4;
    --yellow: #ffc915;
    --blue: #5db4e8;
    --dark: #141b1f;
    --dark-text: #2c3236;
    --ink: #1a1a1a;
    --rule: #1f5fa8;
    --pale: #fdf8d6;
    --edge: #3a3a3a;
  }
  html, body {
    margin: 0;
    padding: 0;
    overflow: hidden;
    background: var(--page);
  }
  .canvas {
    position: relative;
    width: 1200px;
    height: 613px;
    overflow: hidden;
    background: var(--page);
    font-family: 'Arimo', Arial, sans-serif;
  }
  .slide {
    position: absolute;
    width: 361px;
    height: 271px;
    background: var(--slide);
  }
  .slide-bar {
    position: absolute;
    left: 0; top: 0;
    width: 28px; height: 100%;
    background: var(--orange);
  }
  .slide svg { position: absolute; left: 0; top: 0; }
  .col-1 { left: 32px; }
  .col-2 { left: 425px; }
  .col-3 { left: 822px; }
  .row-1 { top: 22px; }
  .row-2 { top: 324px; }

  .ring-outer { fill: var(--orange); }
  .ring-mid { fill: var(--teal); }
  .ring-inner { fill: var(--yellow); }
  .sector { stroke: #ffffff; stroke-width: 1.6; }
  .sector-on { fill: var(--blue); }
  .sector-off { fill: var(--dark); }

  svg text { font-family: 'Arimo', Arial, sans-serif; fill: var(--ink); }
  .num { font-weight: 700; font-size: 10px; }
  .label { font-size: 5px; }
  .sector-num { font-weight: 700; font-size: 11px; }
  .sector-label { font-size: 4.6px; }
  .muted text, text.muted { fill: var(--dark-text); }

  .org-head { stroke: var(--edge); stroke-width: 1; }
  .org-box { stroke: var(--edge); stroke-width: 0.8; }
  .fill-orange { fill: var(--orange); }
  .fill-teal { fill: var(--teal); }
  .fill-pale { fill: var(--pale); }
  .link { stroke: var(--rule); stroke-width: 1.6; fill: none; }
  .divider { stroke: var(--rule); stroke-width: 2.6; stroke-dasharray: 14 7; }
  .org-title { font-weight: 700; font-size: 10px; }
  .org-role { font-weight: 700; font-size: 6px; }
  .org-name { font-size: 5.6px; }
  .org-zone { font-weight: 700; font-size: 9px; }
</style>
</head>
<body>
<div class="canvas">

  <!-- Four-segment ring: all segments active -->
  <section class="slide col-1 row-1">
    <div class="slide-bar"></div>
    <svg width="361" height="271" viewBox="0 0 361 271">
      <g transform="translate(193 135)">
        <circle class="ring-outer" r="125"/>
        <circle class="ring-mid" r="103"/>
        <circle class="ring-inner" r="83"/>
        <path class="sector sector-on" d="M0,0 L-58,0 A58,58 0 0 1 0,-58 Z"/>
        <path class="sector sector-on" d="M0,0 L0,-58 A58,58 0 0 1 58,0 Z"/>
        <path class="sector sector-on" d="M0,0 L0,58 A58,58 0 0 1 -58,0 Z"/>
        <path class="sector sector-on" d="M0,0 L58,0 A58,58 0 0 1 0,58 Z"/>
        <text x="-21" y="-113" class="num">9</text><text x="-12" y="-116" class="label">Franchise Lawyers</text><text x="-5" y="-110" class="label">Finance</text>
        <text x="-21" y="-89" class="num">8</text><text x="-12" y="-90" class="label">Legal Analysts</text>
        <text x="-21" y="-67" class="num">7</text><text x="-12" y="-68" class="label">Sales&amp;Marketing</text>
        <text x="-21" y="77" class="num">6</text><text x="-12" y="76" class="label">Scientists</text>
        <text x="-53" y="-18" class="sector-num">1</text><text x="-45" y="-22" class="sector-label">HPAC specialists</text><text x="-45" y="-17" class="sector-label">(Med–Commercial</text><text x="-45" y="-12" class="sector-label">Products)</text>
        <text x="4" y="-18" class="sector-num">2</text><text x="13" y="-22" class="sector-label">HPAC specialists</text><text x="13" y="-17" class="sector-label">(Med–Commercial</text><text x="13" y="-12" class="sector-label">Products)</text>
        <text x="-53" y="17" class="sector-num">3</text><text x="-45" y="9" class="sector-label">HPAC specialists</text><text x="-45" y="14" class="sector-label">(Med Products –</text><text x="-45" y="19" class="sector-label">Med Affairs)</text>
        <text x="4" y="17" class="sector-num">4</text><text x="13" y="9" class="sector-label">HPAC specialists</text><text x="13" y="14" class="sector-label">(Bio Science –</text><text x="13" y="19" class="sector-label">Med Affairs)</text>
        <text x="4" y="37" class="sector-num">5</text><text x="13" y="35" class="sector-label">Clinical Trials</text>
      </g>
    </svg>
  </section>

  <!-- Three-segment ring: all segments active -->
  <section class="slide col-2 row-1">
    <div class="slide-bar"></div>
    <svg width="361" height="271" viewBox="0 0 361 271">
      <g transform="translate(180 135)">
        <circle class="ring-outer" r="125"/>
        <circle class="ring-mid" r="103"/>
        <circle class="ring-inner" r="83"/>
        <path class="sector sector-on" d="M0,0 L0,-58 A58,58 0 0 0 -50.2,29 Z"/>
        <path class="sector sector-on" d="M0,0 L0,-58 A58,58 0 0 1 50.2,29 Z"/>
        <path class="sector sector-on" d="M0,0 L-50.2,29 A58,58 0 0 0 50.2,29 Z"/>
        <text x="-26" y="-113" class="num">15</text><text x="-12" y="-118" class="label">Franchise Lawyers</text><text x="-12" y="-112" class="label">Finance</text><text x="-12" y="-106" class="label">Committee Members</text>
        <text x="-26" y="-89" class="num">14</text><text x="-12" y="-90" class="label">Legal Analysts</text>
        <text x="-26" y="-65" class="num">13</text><text x="-12" y="-73" class="label">Physicians</text><text x="-12" y="-67" class="label">Clinicians</text><text x="-12" y="-61" class="label">Scientists</text>
        <text x="0" y="73" class="label" text-anchor="middle">External Orgs</text>
        <text x="-28" y="-15" class="sector-num" text-anchor="middle">10</text><text x="-28" y="-8" class="sector-label" text-anchor="middle">HPAC specialists</text><text x="-28" y="-3" class="sector-label" text-anchor="middle">(Med Products –</text><text x="-28" y="2" class="sector-label" text-anchor="middle">Med Affairs)</text>
        <text x="28" y="-15" class="sector-num" text-anchor="middle">11</text><text x="28" y="-8" class="sector-label" text-anchor="middle">HPAC specialists</text><text x="28" y="-3" class="sector-label" text-anchor="middle">(Bio Science –</text><text x="28" y="2" class="sector-label" text-anchor="middle">Med Affairs)</text>
        <text x="0" y="30" class="sector-num" text-anchor="middle">12</text><text x="0" y="36" class="sector-label" text-anchor="middle">HPAC specialists</text><text x="0" y="41" class="sector-label" text-anchor="middle">(Contributions</text><text x="0" y="46" class="sector-label" text-anchor="middle">Management</text><text x="0" y="51" class="sector-label" text-anchor="middle">Program)</text>
      </g>
    </svg>
  </section>

  <!-- Organisation chart -->
  <section class="slide col-3 row-1">
    <svg width="361" height="271" viewBox="0 0 361 271">
      <path class="link" d="M25,70 V193"/>
      <path class="link" d="M25,106 H30"/>
      <path class="link" d="M110,70 V90"/>
      <path class="link" d="M25,196 H30"/>
      <path class="link" d="M241,60 V192"/>
      <path class="link" d="M241,86 H246"/>
      <path class="link" d="M300,84 H308"/>
      <path class="link" d="M210,106 V94 Q210,86 218,86 H241"/>
      <path class="link" d="M241,192 H248"/>
      <line class="divider" x1="0" y1="166" x2="361" y2="166"/>

      <rect class="org-head fill-orange" x="21" y="26" width="101" height="44"/>
      <text x="71.5" y="51" class="org-title" text-anchor="middle">Medical Products</text>
      <rect class="org-head fill-teal" x="240" y="23" width="98" height="37"/>
      <text x="289" y="45" class="org-title" text-anchor="middle">Bio Science</text>

      <rect class="org-box fill-orange" x="30" y="88" width="66" height="36" rx="4"/>
      <text x="63" y="99" class="org-role" text-anchor="middle">Medical Affairs</text>
      <text x="63" y="107" class="org-name" text-anchor="middle">Mara Ellison</text>
      <text x="63" y="115" class="org-name" text-anchor="middle">Joan Pruett</text>

      <rect class="org-box fill-orange" x="103" y="90" width="43" height="24" rx="4"/>
      <text x="124.5" y="100" class="org-role" text-anchor="middle">Commercial</text>
      <text x="124.5" y="108" class="org-name" text-anchor="middle">Lena Harwood</text>

      <rect class="org-box fill-teal" x="186" y="106" width="47" height="27" rx="4"/>
      <text x="209.5" y="117" class="org-role" text-anchor="middle">Clinical Trials</text>
      <text x="209.5" y="126" class="org-name" text-anchor="middle">Helen Corrow</text>

      <rect class="org-box fill-teal" x="246" y="72" width="54" height="28" rx="4"/>
      <text x="273" y="83" class="org-role" text-anchor="middle">Medical Affairs</text>
      <text x="273" y="92" class="org-name" text-anchor="middle">Tomas Reyler</text>

      <rect class="org-box fill-teal" x="308" y="72" width="50" height="28" rx="4"/>
      <text x="333" y="80" class="org-role" text-anchor="middle">Commercial</text>
      <text x="333" y="88" class="org-name" text-anchor="middle">Ivo Stanek</text>
      <text x="333" y="95" class="org-name" text-anchor="middle">Greta Vail</text>

      <text x="168" y="201" class="org-zone" text-anchor="middle">External</text>

      <rect class="org-box fill-orange" x="30" y="180" width="54" height="32" rx="4"/>
      <text x="57" y="190" class="org-role" text-anchor="middle">Medical Affairs</text>
      <text x="57" y="198" class="org-name" text-anchor="middle">Nadia Burke</text>
      <text x="57" y="206" class="org-name" text-anchor="middle">Ruth Okafor</text>

      <rect class="org-box fill-teal" x="248" y="183" width="48" height="24" rx="4"/>
      <text x="272" y="193" class="org-role" text-anchor="middle">Medical Affairs</text>
      <text x="272" y="201" class="org-name" text-anchor="middle">Sana Qadir</text>

      <rect class="org-box fill-pale" x="135" y="224" width="60" height="32" rx="4"/>
      <text x="165" y="234" class="org-role" text-anchor="middle">Contributions</text>
      <text x="165" y="242" class="org-name" text-anchor="middle">Management Team</text>
      <text x="165" y="250" class="org-name" text-anchor="middle">Petra Lindqvist</text>
    </svg>
  </section>

  <!-- Four-segment ring: segment 1 highlighted -->
  <section class="slide col-1 row-2">
    <div class="slide-bar"></div>
    <svg width="361" height="271" viewBox="0 0 361 271">
      <g transform="translate(193 135)">
        <circle class="ring-outer" r="125"/>
        <circle class="ring-mid" r="103"/>
        <circle class="ring-inner" r="83"/>
        <path class="sector sector-on" d="M0,0 L-58,0 A58,58 0 0 1 0,-58 Z"/>
        <path class="sector sector-off" d="M0,0 L0,-58 A58,58 0 0 1 58,0 Z"/>
        <path class="sector sector-off" d="M0,0 L0,58 A58,58 0 0 1 -58,0 Z"/>
        <path class="sector sector-off" d="M0,0 L58,0 A58,58 0 0 1 0,58 Z"/>
        <text x="-21" y="-113" class="num">9</text><text x="-12" y="-116" class="label">Franchise Lawyers</text><text x="-5" y="-110" class="label">Finance</text>
        <text x="-21" y="-89" class="num">8</text><text x="-12" y="-90" class="label">Legal Analysts</text>
        <text x="-21" y="-67" class="num">7</text><text x="-12" y="-68" class="label">Sales&amp;Marketing</text>
        <text x="-21" y="77" class="num">6</text><text x="-12" y="76" class="label">Scientists</text>
        <text x="-53" y="-18" class="sector-num">1</text><text x="-45" y="-22" class="sector-label">HPAC specialists</text><text x="-45" y="-17" class="sector-label">(Med–Commercial</text><text x="-45" y="-12" class="sector-label">Products)</text>
        <g class="muted">
          <text x="4" y="-18" class="sector-num">2</text><text x="13" y="-22" class="sector-label">HPAC specialists</text><text x="13" y="-17" class="sector-label">(Med–Commercial</text><text x="13" y="-12" class="sector-label">Products)</text>
          <text x="-53" y="17" class="sector-num">3</text><text x="-45" y="9" class="sector-label">HPAC specialists</text><text x="-45" y="14" class="sector-label">(Med Products –</text><text x="-45" y="19" class="sector-label">Med Affairs)</text>
          <text x="4" y="17" class="sector-num">4</text><text x="13" y="9" class="sector-label">HPAC specialists</text><text x="13" y="14" class="sector-label">(Bio Science –</text><text x="13" y="19" class="sector-label">Med Affairs)</text>
          <text x="4" y="37" class="sector-num">5</text><text x="13" y="35" class="sector-label">Clinical Trials</text>
        </g>
      </g>
    </svg>
  </section>

  <!-- Four-segment ring: segment 2 highlighted -->
  <section class="slide col-2 row-2">
    <div class="slide-bar"></div>
    <svg width="361" height="271" viewBox="0 0 361 271">
      <g transform="translate(180 135)">
        <circle class="ring-outer" r="125"/>
        <circle class="ring-mid" r="103"/>
        <circle class="ring-inner" r="83"/>
        <path class="sector sector-off" d="M0,0 L-58,0 A58,58 0 0 1 0,-58 Z"/>
        <path class="sector sector-on" d="M0,0 L0,-58 A58,58 0 0 1 58,0 Z"/>
        <path class="sector sector-off" d="M0,0 L0,58 A58,58 0 0 1 -58,0 Z"/>
        <path class="sector sector-off" d="M0,0 L58,0 A58,58 0 0 1 0,58 Z"/>
        <text x="-21" y="-113" class="num">9</text><text x="-12" y="-116" class="label">Franchise Lawyers</text><text x="-5" y="-110" class="label">Finance</text>
        <text x="-21" y="-89" class="num">8</text><text x="-12" y="-90" class="label">Legal Analysts</text>
        <text x="-21" y="-67" class="num">7</text><text x="-12" y="-68" class="label">Sales&amp;Marketing</text>
        <text x="-21" y="77" class="num">6</text><text x="-12" y="76" class="label">Scientists</text>
        <text x="4" y="-18" class="sector-num">2</text><text x="13" y="-22" class="sector-label">HPAC specialists</text><text x="13" y="-17" class="sector-label">(Med–Commercial</text><text x="13" y="-12" class="sector-label">Products)</text>
        <g class="muted">
          <text x="-53" y="-18" class="sector-num">1</text><text x="-45" y="-22" class="sector-label">HPAC specialists</text><text x="-45" y="-17" class="sector-label">(Med–Commercial</text><text x="-45" y="-12" class="sector-label">Products)</text>
          <text x="-53" y="17" class="sector-num">3</text><text x="-45" y="9" class="sector-label">HPAC specialists</text><text x="-45" y="14" class="sector-label">(Med Products –</text><text x="-45" y="19" class="sector-label">Med Affairs)</text>
          <text x="4" y="17" class="sector-num">4</text><text x="13" y="9" class="sector-label">HPAC specialists</text><text x="13" y="14" class="sector-label">(Bio Science –</text><text x="13" y="19" class="sector-label">Med Affairs)</text>
          <text x="4" y="37" class="sector-num">5</text><text x="13" y="35" class="sector-label">Clinical Trials</text>
        </g>
      </g>
    </svg>
  </section>

  <!-- Three-segment ring: segment 10 highlighted -->
  <section class="slide col-3 row-2">
    <div class="slide-bar"></div>
    <svg width="361" height="271" viewBox="0 0 361 271">
      <g transform="translate(178 136)">
        <circle class="ring-outer" r="125"/>
        <circle class="ring-mid" r="103"/>
        <circle class="ring-inner" r="83"/>
        <path class="sector sector-on" d="M0,0 L0,-58 A58,58 0 0 0 -50.2,29 Z"/>
        <path class="sector sector-off" d="M0,0 L0,-58 A58,58 0 0 1 50.2,29 Z"/>
        <path class="sector sector-off" d="M0,0 L-50.2,29 A58,58 0 0 0 50.2,29 Z"/>
        <text x="-26" y="-113" class="num">15</text><text x="-12" y="-118" class="label">Franchise Lawyers</text><text x="-12" y="-112" class="label">Finance</text><text x="-12" y="-106" class="label">Committee Members</text>
        <text x="-26" y="-89" class="num">14</text><text x="-12" y="-90" class="label">Legal Analysts</text>
        <text x="-26" y="-65" class="num">13</text><text x="-12" y="-73" class="label">Physicians</text><text x="-12" y="-67" class="label">Clinicians</text><text x="-12" y="-61" class="label">Scientists</text>
        <text x="0" y="73" class="label" text-anchor="middle">External Orgs</text>
        <text x="-28" y="-15" class="sector-num" text-anchor="middle">10</text><text x="-28" y="-8" class="sector-label" text-anchor="middle">HPAC specialists</text><text x="-28" y="-3" class="sector-label" text-anchor="middle">(Med Products –</text><text x="-28" y="2" class="sector-label" text-anchor="middle">Med Affairs)</text>
        <g class="muted">
          <text x="28" y="-15" class="sector-num" text-anchor="middle">11</text><text x="28" y="-8" class="sector-label" text-anchor="middle">HPAC specialists</text><text x="28" y="-3" class="sector-label" text-anchor="middle">(Bio Science –</text><text x="28" y="2" class="sector-label" text-anchor="middle">Med Affairs)</text>
          <text x="0" y="30" class="sector-num" text-anchor="middle">12</text><text x="0" y="36" class="sector-label" text-anchor="middle">HPAC specialists</text><text x="0" y="41" class="sector-label" text-anchor="middle">(Contributions</text><text x="0" y="46" class="sector-label" text-anchor="middle">Management</text><text x="0" y="51" class="sector-label" text-anchor="middle">Program)</text>
        </g>
      </g>
    </svg>
  </section>

</div>
</body>
</html>
```